Simple Modern Label for a Coconut oil product

We need a label designed for Organic Coconut oil. We would like the label to convey the gourmet/high quality product. It should be modern and simple and look like an artisinal product. The label will need to contain all the basic label requirements - Independence list, place for nutrition facts, our company logo etc.
The label will ultimately be printed as oil proof, so it will have a glossy appearance.
I have includes some examples that I like and a file with the logo.

Product Container - Wide Mount Clear Glass Jar: 4.75 inches tall (base to the bottom of the lid) and 9.5 in circumference
Label: Can be 1 or 2 separate labels, round, square and rectangle are okay
No larger than 3 inches high and 9 inches long

Target Market(s)

Middle Age home chef

Industry/Entity Type

Product

Requirements
Must have
• - logo (Attached below, I have this in multiple formats, let me know if you need them)
• - 14 FL OZ (414mL)
• - ingredient: organic unrefined whole kernel virgin coconut oil,
• - Manufacturer: XXX Y St., anywhere, CA, 99999
• - Distributed by Meadowfern Naturals, P.O. Box 5521, Oakland, CA 94612 www.MeadowfernNaturals.example
• - Certified Organic by Company Name
• - Product of Sri Lanka
Nice to have
• - Nutrition Facts
Should not have
• Clutter

```html
<!DOCTYPE html>
<html lang="en">
<head>
<meta charset="utf-8">
<title>Meadowfern Naturals – Virgin Coconut Oil Label</title>
<link rel="stylesheet" href="https://fonts.googleapis.com/css2?family=Josefin+Sans:wght@300;400&display=swap">
<style>
  :root {
    --page: #ffffff;
    --navy: #14244b;
    --navy-light: #233766;
    --gold: #f3c92c;
    --gold-deep: #d6a91f;
    --gold-pale: #f7dc6a;
    --ink-dark: #1c2640;
    --cream: #ffffff;
    --coconut-brown: #7a4a2a;
    --coconut-shell: #a46a3e;
  }
  html, body {
    margin: 0;
    padding: 0;
    width: 1200px;
    height: 914px;
    overflow: hidden;
    background: var(--page);
  }
  .canvas {
    position: relative;
    width: 1200px;
    height: 914px;
  }
  .label {
    position: absolute;
    left: 100px;
    top: 297px;
    width: 1000px;
    height: 320px;
  }
  .brand-name {
    font-family: "Josefin Sans", sans-serif;
    font-weight: 400;
    font-size: 24px;
    fill: var(--ink-dark);
  }
  .net-contents {
    font-family: "Josefin Sans", sans-serif;
    font-weight: 300;
    font-size: 21px;
    fill: var(--ink-dark);
  }
  .title-virgin {
    font-family: "Josefin Sans", sans-serif;
    font-weight: 300;
    font-size: 36px;
    fill: var(--cream);
  }
  .title-coconut {
    font-family: "Josefin Sans", sans-serif;
    font-weight: 300;
    font-size: 58px;
    fill: var(--cream);
  }
  .title-oil {
    font-family: "Josefin Sans", sans-serif;
    font-weight: 300;
    font-size: 52px;
    fill: var(--cream);
  }
</style>
</head>
<body>
<main class="canvas">
  <svg class="label" viewBox="0 0 1000 320" xmlns="http://www.w3.org/2000/svg">
    <defs>
      <linearGradient id="bandShade" x1="0" y1="0" x2="1" y2="0">
        <stop offset="0" stop-color="var(--navy)"/>
        <stop offset="0.7" stop-color="var(--navy)"/>
        <stop offset="1" stop-color="var(--navy-light)"/>
      </linearGradient>
      <linearGradient id="goldShade" x1="0" y1="0" x2="0" y2="1">
        <stop offset="0" stop-color="var(--gold-deep)"/>
        <stop offset="0.55" stop-color="var(--gold)"/>
        <stop offset="1" stop-color="var(--gold-pale)"/>
      </linearGradient>
      <radialGradient id="coconutTone" cx="0.45" cy="0.55" r="0.6">
        <stop offset="0" stop-color="var(--coconut-shell)"/>
        <stop offset="1" stop-color="var(--coconut-brown)"/>
      </radialGradient>
    </defs>

    <!-- navy band -->
    <rect class="band" x="0" y="0" width="1000" height="320" fill="url(#bandShade)"/>

    <!-- gold panel sweeping into a thin rule -->
    <path class="gold-sweep" fill="url(#goldShade)"
      d="M0 0 H229 C300 80 340 158 420 160 H1000 V167 H420 C340 169 300 240 229 320 H0 Z"/>

    <!-- stitched borders -->
    <line class="stitch" x1="0" y1="16" x2="1000" y2="16" stroke="var(--cream)" stroke-width="2" stroke-dasharray="2 4"/>
    <line class="stitch" x1="0" y1="306" x2="1000" y2="306" stroke="var(--cream)" stroke-width="2" stroke-dasharray="2 4"/>

    <!-- brand -->
    <circle class="brand-mark" cx="32" cy="124" r="12" fill="var(--ink-dark)"/>
    <text class="brand-name" x="52" y="132">Meadowfern Naturals</text>

    <!-- net contents -->
    <text class="net-contents" x="49" y="222">14 FL OZ</text>
    <text class="net-contents" x="47" y="252">(414mL)</text>

    <!-- product title -->
    <text class="title-virgin" x="371" y="155">VIRGIN</text>
    <text class="title-coconut" x="288" y="236">COCONUT</text>
    <text class="title-oil" x="651" y="262">Oil</text>

    <!-- coconut illustration area -->
    <ellipse class="illustration" role="img" aria-label="Watercolour illustration of a whole coconut and a halved coconut with a palm frond"
      cx="672" cy="122" rx="110" ry="62" fill="url(#coconutTone)"/>
  </svg>
</main>
</body>
</html>
```